Guiding Your Revenue Overhaul *

Bold eye-catching design for business non-fiction: I am seeking a bold, and clean design for a book. The book will be 6X9 for both the ebook and in print. I am open to ideas, but found that books like “steady as rain” with contrast are highly desirable for business books.

I am open to color choices.

I would also like a growth orientated graphic in the book - something to show growth, leadership, movement. Not just a plain graphic.

The title:

Guiding Your Revenue Overhaul

The subtitle - I am open to suggestions. Two subtitles I am considering:

A framework for new sales leaders and those who want to keep winning.

A guide for new sales leaders and those who want to keep winning.

The below is an introduction of the book: (Back Jacket)

Sales transformation is a topic that is infrequently written about. For the new sales leader, there are a myriad of books written on coaching, leadership, forecasting, solution selling and sales process but very little is written about how to assess a sales team and build a plan for long-term success.

Through my sales leadership career, whether recently promoted or starting with a new team, I have often asked the question: Where do I start?

In the end, I was disappointed with the answers from currently available books and research, left to figure it out myself - which I did over a decade, with great pain and through many transformations. The inability to answer the question – Where do I start? – is why I wrote this book. To answer that question.

The goal of this book is to help sales leaders answer that question by providing a framework to understand the business, build a plan, and guide the team through the different stages of a sales transformation. A framework to succeed at the fastest pace possible, quarter after quarter.

(End back jacket - the rest is just additional context)

Over the last decade, I have had the privilege of leading teams in North America, Europe, and Asia. I have led turnarounds, growth businesses, and realignments. Each team was different in size, complexity, and culture; and each one offered up new and unique challenges. Each team operated with different market dynamics: one was a commodity; one was a low-cost leader; one was a market innovator. Each transformation helped me learn by taking risks, by failing and by succeeding. At each step, I had many teachers; and as I learned, I made notes. Over time I built a framework that you can leverage as you read and absorb this book. As you lead your team through a sales transformation.

I hope that this book will become for you what The Copper Lantern is for me: a favorite on your bookshelf; underlined, highlighted, dog-eared, and an ongoing reference.

Sales leadership is a journey. It is never linear, and it is always changing. At different times, different parts of this book will apply, while others will not, but hopefully, you will find it a useful and long-lasting reference.

Target Market(s)

Business readers. Sales leaders.

Requirements
Must have
• Modern, clear, eye catching colours. Clean. Graphics that indicate growth, leadership, strength.
• Please ensure the design has the full cover and back jacket design. Please use the introduction of the book as the back jacket text.

```html
<!DOCTYPE html>
<html lang="en">
<head>
<meta charset="utf-8">
<title>Guiding Your Revenue Overhaul – Cover Spread</title>
<link rel="stylesheet" href="https://fonts.googleapis.com/css2?family=Oswald:wght@400;500;700&family=Open+Sans:wght@400;600&display=swap">
<style>
  :root {
    --page-bg: #eeeeee;
    --paper: #ffffff;
    --ink: #1c1c1c;
    --muted: #8a8a8a;
    --red: #d7141a;
    --red-dark: #a80e13;
    --spine-line: #e3e3e3;
  }
  * { box-sizing: border-box; margin: 0; padding: 0; }
  html, body { width: 900px; height: 1200px; overflow: hidden; }
  body {
    background: var(--page-bg);
    display: flex;
    align-items: center;
    justify-content: center;
    font-family: "Open Sans", Arial, sans-serif;
  }
  .cover-spread {
    width: 880px;
    height: 620px;
    display: flex;
    background: var(--paper);
    box-shadow: 0 2px 10px rgba(0,0,0,0.12);
  }

  /* Back jacket */
  .back-cover {
    width: 410px;
    padding: 46px 30px 30px 34px;
  }
  .back-blurb p {
    font-size: 11.6px;
    line-height: 1.62;
    color: var(--ink);
    margin-bottom: 13px;
  }
  .back-blurb p.closing { color: var(--red); }

  /* Spine */
  .spine {
    width: 60px;
    border-left: 1px solid var(--spine-line);
    border-right: 1px solid var(--spine-line);
    display: flex;
    flex-direction: column;
    align-items: center;
    padding: 22px 0;
  }
  .spine-title, .spine-author {
    writing-mode: vertical-rl;
    font-family: "Oswald", "Arial Narrow", sans-serif;
    text-transform: uppercase;
    white-space: nowrap;
  }
  .spine-title { font-size: 27px; font-weight: 700; letter-spacing: 0.5px; }
  .spine-title .accent { color: var(--red); }
  .spine-title .rest { color: var(--ink); font-weight: 500; }
  .spine-author {
    margin-top: auto;
    font-size: 18px;
    color: var(--muted);
    letter-spacing: 2px;
  }

  /* Front cover */
  .front-cover {
    width: 410px;
    position: relative;
    padding: 30px 26px 0 26px;
  }
  .author-name {
    font-family: "Oswald", "Arial Narrow", sans-serif;
    font-weight: 400;
    font-size: 36px;
    letter-spacing: 6px;
    color: var(--muted);
    text-align: center;
  }
  .hero-art {
    position: absolute;
    left: 170px;
    top: 96px;
    width: 220px;
    height: 290px;
    border-radius: 6px;
    background: linear-gradient(160deg, #f3f3f3 0%, #d9d9d9 55%, #e85a5e 100%);
  }
  .growth-arrow {
    position: absolute;
    left: 150px;
    top: 86px;
  }
  .book-title {
    position: absolute;
    left: 26px;
    top: 380px;
    font-family: "Oswald", "Arial Narrow", sans-serif;
    text-transform: uppercase;
  }
  .book-title .title-lead {
    display: block;
    font-size: 92px;
    font-weight: 700;
    line-height: 1;
    color: var(--red);
    letter-spacing: 1px;
  }
  .book-title .title-rest {
    display: block;
    font-size: 31px;
    font-weight: 500;
    line-height: 1.15;
    color: var(--ink);
    letter-spacing: 0.5px;
  }
  .subtitle {
    position: absolute;
    left: 26px;
    right: 26px;
    top: 548px;
    font-family: "Oswald", "Arial Narrow", sans-serif;
    font-size: 14px;
    letter-spacing: 1.2px;
    text-transform: uppercase;
    color: var(--red);
    line-height: 1.4;
  }
</style>
</head>
<body>
  <div class="cover-spread">
    <section class="back-cover">
      <div class="back-blurb">
        <p>Sales transformation is a topic that is infrequently written about. For the new sales leader, there are a myriad of books written on coaching, leadership, forecasting, solution selling and sales process but very little is written about how to assess a sales team and build a plan for long-term success.</p>
        <p>Through my sales leadership career, whether recently promoted or starting with a new team, I have often asked the question: Where do I start?</p>
        <p>In the end, I was disappointed with the answers from currently available books and research, left to figure it out myself - which I did over a decade, with great pain and through many transformations. The inability to answer the question – Where do I start? – is why I wrote this book. To answer that question.</p>
        <p class="closing">The goal of this book is to help sales leaders answer that question by providing a framework to understand the business, build a plan, and guide the team through the different stages of a sales transformation. A framework to succeed at the fastest pace possible, quarter after quarter.</p>
      </div>
    </section>

    <aside class="spine">
      <div class="spine-title"><span class="accent">Guiding</span> <span class="rest">Your Revenue Overhaul</span></div>
      <div class="spine-author">Author Name</div>
    </aside>

    <section class="front-cover">
      <div class="author-name">AUTHOR NAME</div>
      <div class="hero-art" role="img" aria-label="Illustration of a business leader in a dark suit holding a tablet, with a rising red growth arrow behind him"></div>
      <svg class="growth-arrow" width="150" height="150" viewBox="0 0 150 150" aria-hidden="true">
        <path d="M10 140 L60 80 L85 100 L125 40" fill="none" stroke="var(--red)" stroke-width="12" stroke-linejoin="miter"/>
        <polygon points="108,30 142,18 134,54" fill="var(--red)"/>
      </svg>
      <h1 class="book-title">
        <span class="title-lead">Guiding</span>
        <span class="title-rest">Your Revenue Overhaul</span>
      </h1>
      <p class="subtitle">A framework for new sales leaders and those who want to keep winning</p>
    </section>
  </div>
</body>
</html>
```